Small but growing painting company. Have built up a steady client base. Want to start having a more professional look. Want to start with changing my business cards, and also getting new logo and tee shirts.

Target Market(s)

Home owners, property management companies, all ages 30-70

Industry/Entity Type

Painting And Decorating

Contact Information for Business Card

Bright Ridge Painting LLC Derek Vanstrand 630-485-7039 interior, exterior, vaulted ceiling, drywall repair, pressure washing, kitchen cabinets, epoxy, garage floors,

Font styles to use
Sans Serif
Other font styles liked:
• Harrington

Colors
0355a3
ffffff
ec1f27
000000
3176b5
0493ce
474747
b7b7b7

Requirements
Must have
• Creative, something that doesn’t look like every other painting card.
Nice to have
• I would like something with an arrow or something going to a point

```html
<!DOCTYPE html>
<html lang="en">
<head>
<meta charset="utf-8">
<title>Bright Ridge Painting LLC – Business Cards</title>
<link rel="stylesheet" href="https://fonts.googleapis.com/css2?family=Exo+2:wght@400;500;600&display=swap">
<style>
  :root {
    --bg: #1b1c20;
    --card: #25282b;
    --card-shade: #2c2f33;
    --white: #ffffff;
    --blue: #0493ce;
    --muted: #b7b7b7;
  }
  * { margin: 0; padding: 0; box-sizing: border-box; }
  html, body { width: 1200px; height: 800px; overflow: hidden; background: var(--bg); }
  body { position: relative; font-family: "Exo 2", sans-serif; color: var(--white); }

  .card {
    position: absolute;
    width: 540px;
    height: 308px;
    background: var(--card);
    overflow: hidden;
    box-shadow: 0 18px 40px rgba(0,0,0,.55);
  }
  .card--front { left: 90px; top: 70px; }
  .card--back { left: 570px; top: 420px; }

  .front__disc {
    position: absolute;
    left: 150px; top: -20px;
    width: 280px; height: 280px;
    border-radius: 50%;
    background: var(--card-shade);
  }

  .brand { position: absolute; display: flex; align-items: center; gap: 16px; }
  .brand__dot {
    width: 22px; height: 22px; border-radius: 50%;
    background: var(--blue); flex: none;
  }
  .brand__name {
    font-weight: 500;
    color: var(--white);
    line-height: 1.15;
    letter-spacing: 1px;
  }
  .card--front .brand { left: 110px; top: 112px; }
  .card--front .brand__name { font-size: 30px; }

  .front__web {
    position: absolute;
    left: 148px; top: 212px;
    font-size: 13px;
    letter-spacing: .5px;
    color: var(--white);
  }
  .front__web span { color: var(--blue); }

  .card--back .brand { left: 46px; top: 60px; }
  .card--back .brand__name { font-size: 28px; }

  .back__rule {
    position: absolute;
    left: 60px; top: 168px;
    width: 440px; height: 1px;
    background: var(--blue);
  }
  .person { position: absolute; left: 60px; top: 128px; }
  .person__name { font-size: 22px; font-weight: 500; letter-spacing: .5px; }
  .person__role { position: absolute; left: 60px; top: 174px; font-size: 13px; color: var(--blue); letter-spacing: 1px; }

  .contacts { position: absolute; left: 60px; top: 200px; list-style: none; }
  .contacts li {
    display: flex; align-items: center; gap: 10px;
    font-size: 13px; letter-spacing: .4px; height: 26px;
  }
  .contacts svg { width: 18px; height: 18px; flex: none; }

  .address {
    position: absolute; right: 36px; top: 52px;
    text-align: right; font-size: 13px; line-height: 1.6; letter-spacing: .4px;
  }
</style>
</head>
<body>

  <section class="card card--front" aria-label="Business card front">
    <div class="front__disc"></div>
    <div class="brand">
      <span class="brand__dot"></span>
      <span class="brand__name">Bright Ridge<br>Painting LLC</span>
    </div>
    <p class="front__web">www.<span>brightridgepaint</span>.com</p>
  </section>

  <section class="card card--back" aria-label="Business card back">
    <div class="brand">
      <span class="brand__dot"></span>
      <span class="brand__name">Bright Ridge<br>Painting LLC</span>
    </div>

    <p class="address">PO BOX 418 Harlow Lane<br>2nd street Fairview</p>

    <div class="person"><p class="person__name">Derek Vanstrand</p></div>
    <div class="back__rule"></div>
    <p class="person__role">CEO</p>

    <ul class="contacts">
      <li>
        <svg viewBox="0 0 18 18" aria-hidden="true"><circle cx="9" cy="9" r="8" fill="none" stroke="#0493ce" stroke-width="1.2"/><rect x="6.5" y="4.5" width="5" height="9" rx="1" fill="none" stroke="#fff" stroke-width="1"/></svg>
        630-485-7039
      </li>
      <li>
        <svg viewBox="0 0 18 18" aria-hidden="true"><circle cx="9" cy="9" r="8" fill="none" stroke="#0493ce" stroke-width="1.2"/><rect x="5" y="6" width="8" height="6" fill="none" stroke="#fff" stroke-width="1"/><path d="M5 6 L9 9.5 L13 6" fill="none" stroke="#fff" stroke-width="1"/></svg>
        info@brightridgepaint.com
      </li>
      <li>
        <svg viewBox="0 0 18 18" aria-hidden="true"><circle cx="9" cy="9" r="8" fill="none" stroke="#0493ce" stroke-width="1.2"/><circle cx="9" cy="9" r="4.5" fill="none" stroke="#fff" stroke-width="1"/><path d="M4.5 9 H13.5 M9 4.5 V13.5" stroke="#fff" stroke-width="1"/></svg>
        www.brightridgepaint.com
      </li>
    </ul>
  </section>

</body>
</html>
```